Ostrel Appraisals BV business cards (a financial services company)

I am looking for a business card design that stands out in the financial advisory field of business & intellectual property valuation. The business card design should be conservative, yet different. Address details have changed since the attached business card. New address is:

Molenvlietkade 27
4817 KT Leiden
The Netherlands

Telephone number remains the same.

```html
<!DOCTYPE html>
<html lang="en">
<head>
<meta charset="utf-8">
<title>Ostrel Appraisals BV — Business Cards</title>
<link href="https://fonts.googleapis.com/css2?family=Lato:wght@300;400;700;900&display=swap" rel="stylesheet">
<style>
  :root {
    --stage: #e6e4e1;
    --card-white: #ffffff;
    --card-shade: #f1f1f1;
    --back-grey: #7b7b7d;
    --back-grey-dark: #6c6c6e;
    --ink-dark: #3f4144;
    --ink-mid: #6a6b6e;
    --ink-soft: #8c8d90;
    --rule: #8f9093;
    --band-dark: #4a4d51;
    --band-light: #9a9a9c;
    --icon-bg: #8a8b8e;
  }
  * { box-sizing: border-box; margin: 0; padding: 0; }
  html, body {
    width: 1200px; height: 900px; overflow: hidden;
    background: var(--stage);
    font-family: "Lato", Arial, sans-serif;
  }
  .stage {
    position: relative; width: 1200px; height: 900px;
  }
  .card {
    position: absolute; left: 260px; width: 680px; height: 390px;
    box-shadow: 0 6px 18px rgba(0,0,0,0.18);
    overflow: hidden;
  }
  /* Back side */
  .card-back {
    top: 40px;
    background: linear-gradient(135deg, var(--back-grey) 0%, var(--back-grey-dark) 100%);
    display: flex; align-items: center; justify-content: center;
  }
  .back-wordmark {
    color: #ffffff; font-weight: 300; font-size: 46px;
    letter-spacing: 3px; text-transform: uppercase;
  }
  /* Front side */
  .card-front {
    top: 470px;
    background: linear-gradient(180deg, var(--card-white) 0%, var(--card-shade) 100%);
  }
  .front-wordmark {
    position: absolute; right: 40px; top: 52px;
    color: var(--ink-mid); font-weight: 400; font-size: 24px;
    letter-spacing: 1.5px; text-transform: uppercase;
  }
  .person-name {
    position: absolute; left: 40px; top: 128px;
    color: var(--ink-mid); font-weight: 900; font-size: 34px; letter-spacing: 3px;
    text-transform: uppercase;
  }
  .credentials {
    position: absolute; right: 40px; top: 128px; text-align: right;
  }
  .credentials .letters {
    color: var(--ink-dark); font-weight: 700; font-size: 17px; letter-spacing: 1.5px;
  }
  .credentials .role {
    color: var(--ink-soft); font-weight: 400; font-size: 15px; letter-spacing: 2px;
    text-transform: uppercase; margin-top: 2px;
  }
  .divider {
    position: absolute; left: 40px; right: 40px; top: 185px;
    height: 2px; background: var(--rule);
  }
  .contact-list {
    position: absolute; left: 40px; top: 206px; list-style: none;
  }
  .contact-list li, .address li {
    display: flex; align-items: center; gap: 10px;
    color: var(--ink-mid); font-size: 15.5px; height: 26px;
  }
  .icon {
    width: 18px; height: 18px; background: var(--icon-bg);
    border-radius: 2px; display: flex; align-items: center; justify-content: center;
    flex: none;
  }
  .address {
    position: absolute; right: 40px; top: 206px; list-style: none; text-align: right;
  }
  .address li { justify-content: flex-end; }
  .address .spacer { width: 18px; flex: none; }
  .band {
    position: absolute; bottom: 0; height: 30px;
  }
  .band-dark { left: 0; width: 400px; background: var(--band-dark); }
  .band-light { left: 408px; right: 0; background: var(--band-light); }
</style>
</head>
<body>
<main class="stage">

  <section class="card card-back" aria-label="Business card, back side">
    <span class="back-wordmark">Ostrel Appraisals</span>
  </section>

  <section class="card card-front" aria-label="Business card, front side">
    <span class="front-wordmark">Ostrel Appraisals</span>

    <h1 class="person-name">Maarten Keel</h1>

    <div class="credentials">
      <div class="letters">CFA, ASA, RV</div>
      <div class="role">Managing Director</div>
    </div>

    <div class="divider"></div>

    <ul class="contact-list">
      <li>
        <span class="icon">
          <svg width="12" height="12" viewBox="0 0 12 12"><path d="M3 1 L5 3.5 L4 5 Q5 7 7 8 L8.5 7 L11 9 L9.5 11 Q5 11 1 4.5 Q1 2 3 1 Z" fill="#fff"/></svg>
        </span>
        +31 (0)70 555 0142
      </li>
      <li>
        <span class="icon">
          <svg width="12" height="10" viewBox="0 0 12 10"><rect x="0.5" y="0.5" width="11" height="9" fill="none" stroke="#fff"/><path d="M0.5 0.5 L6 5.5 L11.5 0.5" fill="none" stroke="#fff"/></svg>
        </span>
        mkeel@ostrelappraisals.com
      </li>
      <li>
        <span class="icon">
          <svg width="12" height="12" viewBox="0 0 12 12"><circle cx="6" cy="6" r="5" fill="none" stroke="#fff"/><ellipse cx="6" cy="6" rx="2.2" ry="5" fill="none" stroke="#fff"/><path d="M1 6 H11" stroke="#fff"/></svg>
        </span>
        www.ostrelappraisals.com
      </li>
    </ul>

    <ul class="address">
      <li>
        Molenvlietkade 27
        <span class="icon">
          <svg width="10" height="12" viewBox="0 0 10 12"><path d="M5 11.5 Q0.5 6.5 0.5 4.5 A4.5 4.5 0 0 1 9.5 4.5 Q9.5 6.5 5 11.5 Z" fill="#fff"/><circle cx="5" cy="4.5" r="1.6" fill="#8a8b8e"/></svg>
        </span>
      </li>
      <li>4817 KT Leiden<span class="spacer"></span></li>
      <li>The Netherlands<span class="spacer"></span></li>
    </ul>

    <div class="band band-dark"></div>
    <div class="band band-light"></div>
  </section>

</main>
</body>
</html>
```